Corvane Project Services - Flyer

Project Breif:
I need a single page A4 Capability Statement, which will be used to market our services to prospective clients, both in print and via email PDF.
It needs to look professional and should incorporate the elements I have uploaded into files, these include:
Capability Statement Text
Corvane Services Company Logo
Additional Logo’s (Tools We Use)
Glimmer Bay Pics can be cut into the page
I have included examples of capability statements as a guide to what i am looking for.
Regards
Derek
Engineering Consulting

```html
<!DOCTYPE html>
<html lang="en">
<head>
<meta charset="utf-8">
<title>Corvane Project Services – Capability Statement</title>
<link href="https://fonts.googleapis.com/css2?family=Open+Sans:wght@300;400;600;700&display=swap" rel="stylesheet">
<style>
  :root {
    --blue: #2f7fc4;
    --blue-deep: #2a5b9c;
    --blue-text: #3467a8;
    --sky: #8fcdee;
    --sky-pale: #cfe8f6;
    --band: #3a84c9;
    --page: #e8edf1;
    --white: #ffffff;
    --ink: #1d2a38;
    --bullet: #9fd3ef;
  }
  * { box-sizing: border-box; margin: 0; padding: 0; }
  html, body { width: 848px; height: 1200px; overflow: hidden; }
  body {
    font-family: "Open Sans", Arial, sans-serif;
    background: linear-gradient(180deg, #f7f9fb 0%, var(--page) 45%, #dfe5ea 100%);
    position: relative;
    color: var(--ink);
  }
  .title-card {
    position: absolute; left: 0; top: 0; width: 548px; height: 143px;
    background: var(--white);
    border-bottom-right-radius: 60px;
    box-shadow: 0 2px 8px rgba(0,0,0,.08);
  }
  .title-card h1 {
    position: absolute; left: 107px; top: 46px;
    font-weight: 400; font-size: 29px; line-height: 40px;
    color: var(--blue);
  }
  .brand {
    position: absolute; left: 594px; top: 36px; width: 190px;
    text-align: center;
  }
  .brand-mark {
    width: 62px; height: 62px; border-radius: 50%;
    background: var(--blue); margin: 0 auto 8px;
  }
  .brand-name {
    font-size: 12px; font-weight: 700; letter-spacing: 1px;
    color: var(--ink); line-height: 16px;
  }
  .top-stripe {
    position: absolute; left: 0; top: 150px; width: 848px; height: 12px;
    background: var(--sky);
  }
  .hero {
    position: absolute; left: 0; top: 162px; width: 848px; height: 222px;
    background: linear-gradient(100deg, #eef3f8 0%, #d6e2ee 40%, #c7d6e4 70%, #e3ebf2 100%);
  }
  .about-tab {
    position: absolute; left: 435px; top: 336px; width: 413px; height: 56px;
    background: var(--band);
    border-top-left-radius: 28px;
    color: var(--white);
    font-size: 36px; letter-spacing: 3px; font-weight: 400;
    padding-left: 96px; line-height: 56px;
  }
  .services-card {
    position: absolute; left: 26px; top: 378px; width: 366px; height: 612px;
    background: var(--white);
    border-top-right-radius: 60px;
    border-bottom-right-radius: 24px;
    padding: 36px 0 0 30px;
    box-shadow: 0 2px 8px rgba(0,0,0,.08);
  }
  .services-card h2 {
    font-size: 26px; font-weight: 400; color: var(--blue); line-height: 32px;
    margin-bottom: 8px;
  }
  .services-card h3 {
    font-size: 23px; font-weight: 400; color: var(--blue-deep); line-height: 30px;
    margin: 2px 0 6px -2px;
  }
  .service-list { list-style: none; margin: 0 0 4px 0; }
  .service-list li {
    position: relative; padding-left: 30px;
    font-size: 13.5px; line-height: 23.2px; color: var(--blue-deep);
  }
  .service-list li::before {
    content: ""; position: absolute; left: 8px; top: 7px;
    width: 10px; height: 10px; border-radius: 50%; background: var(--bullet);
  }
  .contact-card {
    position: absolute; left: 26px; top: 1012px; width: 366px; height: 164px;
    background: var(--sky);
    border-top-left-radius: 44px;
    border-bottom-right-radius: 10px;
    padding: 16px 28px 0 0; text-align: right;
  }
  .contact-card h2 {
    font-size: 25px; font-weight: 400; color: var(--ink); line-height: 34px;
    margin-right: 28px; margin-bottom: 4px;
  }
  .contact-line {
    display: flex; justify-content: flex-end; align-items: center; gap: 10px;
    font-size: 19px; line-height: 32px; color: var(--ink);
  }
  .contact-line svg { width: 20px; height: 20px; flex: none; }
  .about-card {
    position: absolute; left: 413px; top: 392px; width: 414px; height: 790px;
    background: var(--white);
    border-bottom-left-radius: 40px;
    border-bottom-right-radius: 40px;
    padding: 28px 32px 0 20px;
    text-align: right;
    box-shadow: 0 2px 8px rgba(0,0,0,.08);
  }
  .about-card p {
    font-size: 13.3px; line-height: 17.5px; color: var(--blue-text);
    margin-bottom: 14px;
  }
  .about-card .intro {
    padding-right: 14px; border-right: 3px solid var(--blue-deep);
  }
  .about-card h3 {
    font-size: 22px; font-weight: 400; color: var(--blue-deep); line-height: 28px;
    margin: 2px 0 4px;
  }
  .tools-heading {
    text-align: left; margin-top: 6px; padding-left: 28px;
    font-size: 16px; font-weight: 400; color: var(--ink); letter-spacing: .5px;
  }
  .tools {
    display: grid; grid-template-columns: 1fr 1fr; row-gap: 22px; column-gap: 20px;
    padding: 18px 0 0 30px; text-align: left;
  }
  .tool {
    display: flex; align-items: center; gap: 8px;
    font-size: 16px; font-weight: 700; color: var(--blue-deep);
  }
  .tool i { width: 12px; height: 12px; background: var(--blue-deep); display: inline-block; }
</style>
</head>
<body>
  <header class="title-card">
    <h1>Capability Statement<br>Services Programme</h1>
  </header>
  <div class="brand">
    <div class="brand-mark"></div>
    <div class="brand-name">CORVANE PROJECT SERVICES</div>
  </div>

  <div class="top-stripe"></div>
  <div class="hero" role="img" aria-label="Photo of project schedule printouts, a pen and hands reviewing documents"></div>
  <div class="about-tab">About Us:</div>

  <section class="services-card">
    <h2>CORE SERVICES:</h2>
    <h3>Planning and Scheduling</h3>
    <ul class="service-list">
      <li>Tender Planning</li>
      <li>Interactive Planning / Pull Planning</li>
      <li>EPCMV Planning &amp; Scheduling</li>
      <li>Schedule Earned Value Management</li>
      <li>Independent Schedule Quality Assessment</li>
      <li>Schedule Risk Analysis (Monte Carlo)</li>
      <li>Training</li>
    </ul>
    <h3>Management of Risk</h3>
    <ul class="service-list">
      <li>Risk Management Policies &amp; Procedures</li>
      <li>Risk Management Strategy</li>
      <li>Risk Registers</li>
      <li>Risk Response and Communication</li>
      <li>Cost &amp; Schedule Risk Analysis (Monte Carlo)</li>
      <li>Risk Management Training</li>
    </ul>
    <h3>Cost Control:</h3>
    <ul class="service-list">
      <li>Estimating &amp; Forecasting</li>
      <li>Earned Value Analysis</li>
      <li>Progress Reporting</li>
      <li>Cost Risk Analysis (Monte Carlo)</li>
    </ul>
  </section>

  <section class="contact-card">
    <h2>Contact:</h2>
    <div class="contact-line">info@corvaneservices.ie
      <svg viewBox="0 0 20 20"><circle cx="10" cy="10" r="10" fill="#2a5b9c"/><rect x="5" y="6.5" width="10" height="7" fill="none" stroke="#fff" stroke-width="1.4"/><path d="M5 6.5l5 4 5-4" fill="none" stroke="#fff" stroke-width="1.4"/></svg>
    </div>
    <div class="contact-line">www.corvaneservices.ie
      <svg viewBox="0 0 20 20"><circle cx="10" cy="10" r="10" fill="#2a5b9c"/><circle cx="10" cy="10" r="5.5" fill="none" stroke="#fff" stroke-width="1.2"/><ellipse cx="10" cy="10" rx="2.3" ry="5.5" fill="none" stroke="#fff" stroke-width="1.2"/><path d="M4.5 10h11" stroke="#fff" stroke-width="1.2"/></svg>
    </div>
    <div class="contact-line">+353 (0)870 555 0142
      <svg viewBox="0 0 20 20"><circle cx="10" cy="10" r="10" fill="#2a5b9c"/><path d="M7 5.5l2 2.5-1.2 1.4c.7 1.3 1.6 2.2 2.9 2.9L12 11l2.5 2-1 1.6c-3.6-.3-7-3.7-7.3-7.3z" fill="#fff"/></svg>
    </div>
  </section>

  <section class="about-card">
    <p class="intro">Our goal is to make successful project delivery more achievable and repeatable. We are continually innovating, evolving and learning, utilizing the latest industry tools and techniques to deliver real value to our clients. We are passionate about empowering organisations to achieve their objectives, on time and on budget.</p>
    <h3>Our Team</h3>
    <p>We use highly experienced industry professionals who engage with our clients to deliver practical and innovative project control solutions.</p>
    <h3>Our Expertise</h3>
    <p>For over 20 years we have been helping our clients to successfully deliver capital projects within the pharmaceutical and biotechnology sectors.</p>
    <p>During this time, we have worked closely with multinational healthcare companies and leading A&amp;E firms, on a variety of business-critical projects.</p>
    <p>Our experience and knowledge of project control gives our client’s unparalleled visibility of Cost, Schedule and Risk through the lifecycle of their projects.</p>
    <p>This visibility allows our clients to make timely informed decisions which increase efficiency and project performance.</p>
    <div class="tools-heading">CORVANE SERVICES COMPANY:</div>
    <div class="tools">
      <div class="tool"><i></i>Orvella Planner</div>
      <div class="tool"><i></i>Taskline</div>
      <div class="tool"><i></i>RiskFrame</div>
      <div class="tool"><i></i>Markpoint Pro</div>
      <div class="tool"><i></i>Stellar Plan</div>
      <div class="tool"></div>
      <div class="tool"><i></i>Verrant Gauge</div>
    </div>
  </section>
</body>
</html>
```